Volmira Logo and business card

We need a business card and logo, we are currently using a logo that we like but would like to be a bit more streamlined. We deal with very high end clients and our business card needs to reflect that. We would love to see and hire somebody that can deliver a very MODERN, simple design. With he main front of the card to be black with either a red lettering or White to provide great contrast. I would like to have a minimalist abstract picture of a heavy machine on it but it is not a requirement ( most likely an Crane ( a bold heron crane with a bucket would be perfect or maybe a vendari 270 XT )) If it keeps in line with being a classic simple, and modern design. Letterpress is also an option where it gives it a great look and texture, the card will be printed on a thick stock. On the back there needs to be a star included somewhere on the card and design, this represents the first generation that started the company back in 1936 therefore it is a sentimental addition ( make it modern and simple)
We do not want a cheesy construction template. We do heavy site work, aka we use excavators, payloaders, off road rok j40 trucks, very big fun toys.
There is a huge chance to get the web design as well for the winning design.
Have fun, cannot wait to see the designs!
In addition, we'd like to point out that our primary need and priority is still the BUSINESS CARD design itself. The logo has to complement the overall look of the business card, but it is secondary to the card's look. Please keep this in mind.
Thank you,
Gerald
Target Market(s)
General Contractors, upscale home owners ( house values of 1M plus)
and commercial property owners.
Projects range from $5000 to 1 million.
Industry/Entity Type
Construction
Requirements
Must have
- Star incorporated into design
Nice to have
- an abstract heavy site work machine ( pics attached) If it keeps in line with being a classic simple, and modern design.
I would like to have black and red on the design since all the lettering on the trucks is red, but i will let the designer take care of that.

```html
<!DOCTYPE html>
<html lang="en">
<head>
<meta charset="utf-8">
<title>Volmira Industries Inc — Logo and Business Card</title>
<link rel="stylesheet" href="https://fonts.googleapis.com/css2?family=Oxygen:wght@400;700&display=swap">
<style>
  :root {
    --brand-red: #d3202a;
    --ink: #111111;
    --card-white: #ffffff;
    --band-top: #dedede;
    --board-top: #f4f4f4;
    --board-bottom: #8d8d8d;
  }
  * { box-sizing: border-box; margin: 0; padding: 0; }
  html, body { width: 1000px; height: 1200px; overflow: hidden; }
  body {
    position: relative;
    background: linear-gradient(to bottom, var(--board-top) 0%, #c9c9c9 40%, var(--board-bottom) 100%);
    font-family: "Oxygen", sans-serif;
    color: var(--ink);
  }

  .wordmark { position: absolute; text-align: right; }
  .wordmark__name {
    display: block;
    font-family: "Oxygen", sans-serif;
    font-weight: 700;
    color: var(--brand-red);
    line-height: 1;
    letter-spacing: 0.04em;
  }
  .wordmark__suffix {
    display: block;
    font-family: "Oxygen", sans-serif;
    font-weight: 400;
    color: var(--ink);
    letter-spacing: 0.08em;
    line-height: 1;
  }

  .wordmark--hero { left: 218px; top: 146px; width: 540px; }
  .wordmark--hero .wordmark__name { font-size: 84px; }
  .wordmark--hero .wordmark__suffix { font-size: 20px; margin-top: 12px; }

  .card {
    position: absolute;
    left: 171px;
    width: 634px;
    height: 352px;
    background: var(--card-white);
    box-shadow: 0 6px 22px rgba(0,0,0,0.28);
    overflow: hidden;
  }
  .card--front { top: 306px; }
  .card--back { top: 722px; }

  .card__band {
    position: absolute;
    left: 0; right: 0; bottom: 0;
    background: linear-gradient(to bottom, var(--band-top) 0%, #f4f4f4 35%, var(--card-white) 70%);
  }
  .card--front .card__band { height: 121px; }
  .card--back .card__band { height: 90px; }

  .card--front .wordmark { right: 42px; top: 270px; }
  .card--front .wordmark__name { font-size: 42px; }
  .card--front .wordmark__suffix { font-size: 13px; margin-top: 6px; }

  .card--back .wordmark { right: 42px; top: 292px; }
  .card--back .wordmark__name { font-size: 28px; }
  .card--back .wordmark__suffix { font-size: 9px; margin-top: 4px; }

  .machine-visual {
    position: absolute;
    right: 0; top: 0;
    width: 218px; height: 180px;
    background: linear-gradient(215deg, #0d0d0d 0%, #1a1a1a 35%, rgba(30,30,30,0.55) 60%, rgba(255,255,255,0) 85%);
  }

  .contact {
    position: absolute;
    left: 42px; top: 217px;
    font-size: 12.5px;
    line-height: 16px;
    color: var(--ink);
  }

  .since {
    position: absolute;
    left: 44px; top: 315px;
    display: flex; align-items: center; gap: 4px;
    font-size: 11px; font-weight: 700;
    color: var(--brand-red);
    letter-spacing: 0.02em;
  }
  .since__star { width: 18px; height: 18px; fill: var(--brand-red); }
</style>
</head>
<body>

  <div class="wordmark wordmark--hero">
    <span class="wordmark__name">VOLMIRA</span>
    <span class="wordmark__suffix">INDUSTRIES INC</span>
  </div>

  <section class="card card--front">
    <div class="card__band"></div>
    <div class="wordmark">
      <span class="wordmark__name">VOLMIRA</span>
      <span class="wordmark__suffix">INDUSTRIES INC</span>
    </div>
  </section>

  <section class="card card--back">
    <div class="machine-visual" role="img" aria-label="Black silhouette of an excavator arm and bucket reaching in from the top right corner"></div>
    <p class="contact">
      Gerald Volmira • Project Manager • +315 402 7718 • gerald@volmira.com<br>
      Unit 9K, Harrowfield, Lanmere, 0419
    </p>
    <div class="card__band"></div>
    <div class="since">
      <span>SINCE</span>
      <svg class="since__star" viewBox="0 0 24 24" aria-hidden="true">
        <polygon points="12,1 14.9,8.6 23,8.9 16.6,13.9 18.9,21.8 12,17.2 5.1,21.8 7.4,13.9 1,8.9 9.1,8.6"/>
      </svg>
      <span>1936</span>
    </div>
    <div class="wordmark">
      <span class="wordmark__name">VOLMIRA</span>
      <span class="wordmark__suffix">INDUSTRIES INC</span>
    </div>
  </section>

</body>
</html>
```